Business Cards for a company that provides webstore services to veterinarians

We need business cards designed for our main service PawCartHub. PawCartHub is a webstore that veterinarian clinics can use to that will allow their clients to purchase products for their pets. Our company is Brivolta Veterinary Solutions (Brivolta Veterinary Solutions). Our mission statement is We love pets! We will do everything possible to facilitate along, healthy and happy relationship with their families.

Target Market(s)

Veterinarians

Industry/Entity Type

Veterinary

Contact Information for Business Card

I would like the design to incorporate the colours our our company. Cards should have room for employee name, title (only necessary in two instances), phone number, mobile number, email address and linkedin symbol and related profile name ie Moira Felton. I would like the PawCartHub logo to appear on one side and Brivolta Veterinary Solutions logo to appear on the other. I will need both an english and french version. I can provide the french translation. Please focus on english version and then we will translate

Colors

Designer to choose colors to be used in the design.

Requirements
Must have
• one side - PawCartHub logo with persons name, phone number, mobile number, email address
• second side - Brivolta Veterinary Solutions logo
• colours should be consistent with our company. colours are as follows:
• Red
• RGB: 190 / 30 / 45
• CYMK: 14 / 100 / 90 /10
• Hex: #BE1E2D
• Gray
• RGB: 88 / 89 / 86
• CYMK: 3 / 2 / 0 /64
• Hex: #585956
Nice to have
• address of company - can be on either side address is 4817 Quillan Street Suite 305 Burlington ON K9R 2M4. Toll free number will vary depending on person
• Linkedin symbol and name of person
• on second side with Brivolta Veterinary Solutions logo our company's mission statement
Should not have
• nothing comes to mind

```html
<!DOCTYPE html>
<html lang="en">
<head>
<meta charset="utf-8">
<title>PawCartHub Business Card</title>
<link rel="stylesheet" href="https://fonts.googleapis.com/css2?family=Roboto:wght@400;500;700&display=swap">
<style>
  :root {
    --brand-red: #BE1E2D;
    --brand-gray: #585956;
    --logo-gray: #8a8b88;
    --card-dark: #1e1e1f;
    --card-light: #f7f7f6;
    --backdrop: #2a2a2b;
    --divider: #b9b9b7;
  }
  * { box-sizing: border-box; margin: 0; padding: 0; }
  html, body { width: 1200px; height: 900px; overflow: hidden; }
  body {
    background: var(--backdrop);
    font-family: "Roboto", Arial, sans-serif;
    display: flex;
    flex-direction: column;
    align-items: center;
    justify-content: center;
    gap: 40px;
  }
  .card {
    width: 640px;
    height: 366px;
    border-radius: 4px;
    position: relative;
  }
  .card-front {
    background: var(--card-dark);
    display: flex;
    flex-direction: column;
    align-items: center;
    justify-content: center;
    gap: 22px;
  }
  .company-mark {
    display: flex;
    align-items: center;
    gap: 12px;
  }
  .company-mark__square {
    width: 16px; height: 16px;
    background: var(--brand-red);
  }
  .company-mark__name {
    color: var(--brand-red);
    font-weight: 500;
    font-size: 30px;
    line-height: 1;
  }
  .store-mark {
    color: var(--logo-gray);
    font-weight: 400;
    font-size: 54px;
    line-height: 1;
  }
  .card-back {
    background: var(--card-light);
  }
  .holder {
    position: absolute;
    right: 352px;
    top: 150px;
    text-align: right;
  }
  .holder__name {
    color: var(--brand-red);
    font-weight: 700;
    font-size: 27px;
    letter-spacing: 0.3px;
  }
  .holder__title {
    color: var(--brand-gray);
    font-weight: 500;
    font-size: 18px;
    margin-top: 2px;
  }
  .divider {
    position: absolute;
    left: 312px;
    top: 138px;
    width: 2px;
    height: 122px;
    background: var(--divider);
  }
  .contacts {
    position: absolute;
    left: 332px;
    top: 144px;
    list-style: none;
  }
  .contacts li {
    display: flex;
    align-items: center;
    gap: 10px;
    height: 23px;
    color: var(--brand-gray);
    font-size: 17px;
  }
  .contacts svg { width: 15px; height: 15px; flex: none; }
  .profile-square {
    width: 15px; height: 15px;
    background: var(--brand-red);
    flex: none;
  }
  .mission {
    position: absolute;
    left: 0; right: 0;
    top: 282px;
    text-align: center;
  }
  .mission__label {
    color: var(--brand-red);
    font-weight: 700;
    font-size: 19px;
  }
  .mission__text {
    color: var(--brand-gray);
    font-size: 19px;
    margin-top: 2px;
  }
</style>
</head>
<body>
  <section class="card card-front">
    <div class="company-mark">
      <span class="company-mark__square"></span>
      <span class="company-mark__name">Brivolta Veterinary Solutions</span>
    </div>
    <div class="store-mark">PawCartHub</div>
  </section>

  <section class="card card-back">
    <div class="holder">
      <div class="holder__name">MOIRA FELTON</div>
      <div class="holder__title">CEO/Founder</div>
    </div>
    <div class="divider"></div>
    <ul class="contacts">
      <li>
        <svg viewBox="0 0 16 16"><path fill="#BE1E2D" d="M3.5 1.5l2.5 0 1 3.5-1.6 1.2a8 8 0 0 0 4.4 4.4L11 9l3.5 1v2.5c0 1-1 2-2 2C6.5 14.5 1.5 9.5 1.5 3.5c0-1 1-2 2-2z"/></svg>
        <span>555 014 2738</span>
      </li>
      <li>
        <svg viewBox="0 0 16 16"><rect x="4" y="1" width="8" height="14" rx="1.5" fill="none" stroke="#BE1E2D" stroke-width="2"/><circle cx="8" cy="12.3" r="1" fill="#BE1E2D"/></svg>
        <span>555 017 6420</span>
      </li>
      <li>
        <svg viewBox="0 0 16 16"><rect x="1" y="3" width="14" height="10" fill="#BE1E2D"/><path d="M1.5 3.5L8 9l6.5-5.5" fill="none" stroke="#f7f7f6" stroke-width="1.4"/></svg>
        <span>moira@pawcarthub</span>
      </li>
      <li>
        <svg viewBox="0 0 16 16"><circle cx="8" cy="8" r="6.5" fill="none" stroke="#BE1E2D" stroke-width="2"/><path d="M1.5 8h13M8 1.5c-3 3.5-3 9.5 0 13M8 1.5c3 3.5 3 9.5 0 13" fill="none" stroke="#BE1E2D" stroke-width="1.3"/></svg>
        <span>www.pawcarthub</span>
      </li>
      <li>
        <span class="profile-square"></span>
        <span>Moira Felton</span>
      </li>
    </ul>
    <div class="mission">
      <div class="mission__label">MISSION STATEMENT</div>
      <div class="mission__text">We love pets!</div>
    </div>
  </section>
</body>
</html>
```